School Hallway Magnetic Display Design for school values

I am looking for a someone to help me design a magnetic hallway display that will hang in the hallway of our small school. There are several elements, including 1. 6ft by 4ft designed magnetic bulletin board, 2. Magnets that will stick to the board. See attachment for which elements belong where. The display will be for our TRAVEK program, which rewards students for demonstrating our school values. We want the display to be beautiful and interactive. We are also rebranding, so we want the design to align with our new fonts and colors. In the attached PDF is an outline of our new brand guidelines. Unfortunately, we don't have the color codes, but I'm hoping that you can match the colors listed. Attached are elements to be used on the board, but please use your creativity to make it more dynamic and visually appealing. For example, the star magnets could be another shape. The TRAVEK magnets must remain the same. I've included two photos of boards at other schools that inspired this project.

Target Market(s)

School Community

Industry/Entity Type

Education

Requirements
Should not have
• School Logo

```html
<!DOCTYPE html>
<html lang="en">
<head>
<meta charset="utf-8">
<title>TRAVEK of the Month – Hallway Display</title>
<link rel="stylesheet" href="https://fonts.googleapis.com/css2?family=Alike&family=Marcellus&display=swap">
<style>
  :root{
    --navy:#224f73;
    --star-navy:#2a5a8f;
    --sky:#afcde4;
    --sun:#fedb7c;
    --coral:#de8972;
    --lavender:#bc9cc5;
    --sage:#d7dfb9;
    --white:#ffffff;
  }
  html,body{margin:0;padding:0;overflow:hidden;background:var(--navy);}
  .board{position:relative;width:1200px;height:800px;overflow:hidden;}
  .board svg{position:absolute;inset:0;display:block;}
  .title-text{font-family:"Marcellus",serif;font-size:84px;fill:var(--white);}
  .value-word{font-family:"Alike",serif;font-size:55px;text-anchor:middle;}
  .value-word .outer{fill:var(--navy);stroke:var(--navy);stroke-width:12px;stroke-linejoin:round;}
  .value-word .inner{fill:var(--navy);stroke-width:5px;stroke-linejoin:round;paint-order:stroke;}
  .school-name{font-family:"Marcellus",serif;font-size:22px;fill:var(--navy);}
</style>
</head>
<body>
<div class="board">
<svg viewBox="0 0 1200 800" width="1200" height="800" xmlns="http://www.w3.org/2000/svg">
  <rect class="backdrop" width="1200" height="800" fill="var(--navy)"/>

  <!-- stripe accents: top edge -->
  <g class="stripes stripes-top">
    <polygon points="705,0 763,0 751,18 693,18" fill="var(--sage)"/>
    <polygon points="779,0 837,0 825,18 767,18" fill="var(--lavender)"/>
    <polygon points="853,0 911,0 899,18 841,18" fill="var(--coral)"/>
    <polygon points="927,0 985,0 973,18 915,18" fill="var(--sun)"/>
    <polygon points="1001,0 1059,0 1047,18 989,18" fill="var(--sky)"/>
  </g>
  <!-- stripe accents: bottom edge -->
  <g class="stripes stripes-bottom">
    <polygon points="236,782 294,782 282,800 224,800" fill="var(--sage)"/>
    <polygon points="310,782 368,782 356,800 298,800" fill="var(--lavender)"/>
    <polygon points="384,782 442,782 430,800 372,800" fill="var(--coral)"/>
    <polygon points="458,782 516,782 504,800 446,800" fill="var(--sun)"/>
    <polygon points="532,782 590,782 578,800 520,800" fill="var(--sky)"/>
  </g>
  <!-- stripe accents: left edge -->
  <g class="stripes stripes-left">
    <polygon points="0,180 22,145 22,235 0,270" fill="var(--sage)"/>
    <polygon points="0,282 22,247 22,337 0,372" fill="var(--lavender)"/>
    <polygon points="0,384 22,349 22,439 0,474" fill="var(--coral)"/>
    <polygon points="0,486 22,451 22,541 0,576" fill="var(--sun)"/>
    <polygon points="0,588 22,553 22,643 0,678" fill="var(--sky)"/>
  </g>
  <!-- stripe accents: right edge -->
  <g class="stripes stripes-right">
    <polygon points="1178,265 1200,230 1200,310 1178,345" fill="var(--sage)"/>
    <polygon points="1178,357 1200,322 1200,402 1178,437" fill="var(--lavender)"/>
    <polygon points="1178,449 1200,414 1200,494 1178,529" fill="var(--coral)"/>
    <polygon points="1178,541 1200,506 1200,586 1178,621" fill="var(--sun)"/>
    <polygon points="1178,633 1200,598 1200,678 1178,713" fill="var(--sky)"/>
  </g>

  <!-- board surface -->
  <rect class="board-surface" x="20" y="17" width="1160" height="766" rx="20" fill="var(--white)" stroke="var(--sun)" stroke-width="3"/>

  <!-- title banner -->
  <g class="title-banner">
    <rect x="79" y="35" width="1041" height="118" rx="59" fill="var(--sky)"/>
    <rect x="90" y="45" width="1019" height="98" rx="49" fill="var(--navy)"/>
    <text class="title-text" x="604" y="126" text-anchor="middle" textLength="910" lengthAdjust="spacingAndGlyphs">TRAVEK OF THE MONTH</text>
  </g>

  <!-- thermometer artwork area -->
  <defs>
    <linearGradient id="thermo-fill" x1="0" y1="0" x2="0" y2="1">
      <stop offset="0" stop-color="var(--navy)"/>
      <stop offset="1" stop-color="#2b5d86"/>
    </linearGradient>
  </defs>
  <rect class="thermometer-art" x="685" y="207" width="131" height="419" rx="36"
        fill="url(#thermo-fill)" stroke="var(--sun)" stroke-width="8"
        role="img" aria-label="Illustration of a thermometer tracking progress"/>

  <!-- value words -->
  <g class="value-word">
    <text class="outer" x="1008" y="236">Equality</text>
    <text class="inner" x="1008" y="236" stroke="var(--lavender)">Equality</text>
  </g>
  <g class="value-word">
    <text class="outer" x="1008" y="334">Community</text>
    <text class="inner" x="1008" y="334" stroke="var(--sage)">Community</text>
  </g>
  <g class="value-word">
    <text class="outer" x="1008" y="425">Peace</text>
    <text class="inner" x="1008" y="425" stroke="var(--sun)">Peace</text>
  </g>
  <g class="value-word">
    <text class="outer" x="1008" y="514">Integrity</text>
    <text class="inner" x="1008" y="514" stroke="var(--lavender)">Integrity</text>
  </g>
  <g class="value-word">
    <text class="outer" x="1008" y="608">Stewardship</text>
    <text class="inner" x="1008" y="608" stroke="var(--sage)">Stewardship</text>
  </g>
  <g class="value-word">
    <text class="outer" x="1008" y="706">Simplicity</text>
    <text class="inner" x="1008" y="706" stroke="var(--sky)">Simplicity</text>
  </g>

  <!-- school name -->
  <g class="school-mark">
    <rect x="46" y="722" width="24" height="24" fill="var(--navy)"/>
    <text class="school-name" x="80" y="742">Maple Grove School</text>
  </g>

  <!-- reward stars -->
  <defs>
    <polygon id="star" points="0,-34 10,-12 34,-9 16,8 21,32 0,20 -21,32 -16,8 -34,-9 -10,-12"
             stroke="var(--sky)" stroke-width="3" stroke-linejoin="round"/>
  </defs>
  <g class="reward-stars">
    <use href="#star" x="371" y="734" fill="var(--sky)"/>
    <use href="#star" x="449" y="734" fill="var(--star-navy)"/>
    <use href="#star" x="527" y="734" fill="var(--sun)"/>
    <use href="#star" x="605" y="734" fill="var(--coral)"/>
    <use href="#star" x="683" y="734" fill="var(--lavender)"/>
    <use href="#star" x="761" y="734" fill="var(--sage)"/>
  </g>
</svg>
</div>
</body>
</html>
```